Natural healthcare clinic needs stationery and business card design

We have had a logo developed by Pixel Harbor and are now looking at utilising it for a new business concept. The concept is a natural healthcare clinic that hosts a number of small businesses. The individual practitioners may want to utilise the host business stationery to provide a consistent message to clients.

I am looking for a stationery design - letterhead, DL brochure template and business card that uses our logo. The business name 'Bright Meadows' is all about getting rhythm back into your life so you can be fit and healthy. The stationery design should reflect this.

There are a couple of requirements for the business card, it needs to be double-sided with black and white back. There should be lines to write appointment times on. The cards may need to be custom named on the front for example Carys Dunmore, Remedial Therapist and Aromatherapist. Therefore if a template can be provided so we can customise this information using MS Publisher, it would be appreciated.

The DL brochure template needs to be A4 folded to DL. I am looking for a consistent brand message that can be utilised to produce our own clinic brochures.

The natural healthcare clinic will host the following types of businesses - remedial massage, pregnancy massage, oncology massage, aromatherapy, acupuncture - as a bit of a guide.

Target Market(s)

25-45 year old male and females who work full time.

Industry/Entity Type

Healthcare

Requirements
Must have
• Use the logo I have already.

```html
<!DOCTYPE html>
<html lang="en">
<head>
<meta charset="utf-8">
<title>Bright Meadows – Business Card</title>
<link rel="stylesheet" href="https://fonts.googleapis.com/css2?family=Arimo:wght@400;700&display=swap">
<style>
  :root {
    --backdrop: #e4e4e4;
    --card: #fbfbfb;
    --green-dark: #2f7a34;
    --green-mid: #5a9a48;
    --green-light: #8fbf6a;
    --brand-olive: #5a4b22;
    --text-green: #3d6b2c;
    --rule: #4c6e2e;
  }
  * { box-sizing: border-box; margin: 0; padding: 0; }
  html, body {
    width: 1200px; height: 900px; overflow: hidden;
    background: radial-gradient(circle at 50% 45%, #f4f4f4 0%, var(--backdrop) 75%);
    font-family: "Arimo", Arial, sans-serif;
  }
  .stage { position: relative; width: 1200px; height: 900px; }
  .card {
    position: absolute;
    width: 640px; height: 366px;
    background: var(--card);
    box-shadow: 0 6px 18px rgba(0,0,0,0.18);
    overflow: hidden;
  }
  .card--contact { left: 240px; top: 50px; }
  .card--brand { left: 320px; top: 468px; }
  .swoosh { position: absolute; inset: 0; width: 100%; height: 100%; }

  .contact-block { position: absolute; left: 48px; top: 118px; color: var(--text-green); }
  .contact-block__name { font-size: 30px; font-weight: 400; line-height: 1; }
  .contact-block__position { font-size: 16px; font-weight: 700; margin-top: 4px; }
  .contact-block__details { list-style: none; margin-top: 22px; font-size: 17px; line-height: 1.2; }

  .card__divider {
    position: absolute; left: 320px; top: 40px;
    width: 2px; height: 170px; background: var(--rule);
  }
  .brand-name {
    color: var(--brand-olive); font-weight: 400; white-space: nowrap;
    display: flex; align-items: center;
  }
  .brand-name__dot {
    display: inline-block; border-radius: 50%; background: var(--green-mid);
  }
  .card--contact .brand-name { position: absolute; left: 348px; top: 96px; font-size: 22px; gap: 8px; }
  .card--contact .brand-name__dot { width: 14px; height: 14px; }
  .card--brand .brand-name { position: absolute; left: 70px; top: 140px; font-size: 50px; gap: 14px; }
  .card--brand .brand-name__dot { width: 28px; height: 28px; }
</style>
</head>
<body>
<main class="stage">

  <section class="card card--contact" aria-label="Business card back with contact details">
    <svg class="swoosh" viewBox="0 0 640 366" aria-hidden="true">
      <defs>
        <linearGradient id="swooshGreenA" x1="0" y1="1" x2="1" y2="0">
          <stop offset="0" stop-color="var(--green-dark)"/>
          <stop offset="1" stop-color="var(--green-light)"/>
        </linearGradient>
      </defs>
      <path d="M40 352 C250 305 480 255 640 160 L640 192 C480 272 260 322 40 352Z" fill="url(#swooshGreenA)"/>
      <path d="M390 272 C510 245 600 170 640 50 L640 130 C590 205 500 252 390 272Z" fill="var(--green-dark)"/>
    </svg>
    <div class="contact-block">
      <h1 class="contact-block__name">Your Name</h1>
      <p class="contact-block__position">Position</p>
      <ul class="contact-block__details">
        <li>Address: xxxxxxxxxxxxxxxx</li>
        <li>Phone: xxxxxxxxxxxxxxxxxx</li>
        <li>Fax:xxxxxxxxxxxxxxxxxxxx</li>
        <li>Email: xxxxxxxxxxxxxxxxxx</li>
      </ul>
    </div>
    <div class="card__divider"></div>
    <p class="brand-name"><span class="brand-name__dot"></span>Bright Meadows</p>
  </section>

  <section class="card card--brand" aria-label="Business card front with brand name">
    <svg class="swoosh" viewBox="0 0 640 366" aria-hidden="true">
      <defs>
        <linearGradient id="swooshGreenB" x1="0" y1="1" x2="1" y2="0">
          <stop offset="0" stop-color="var(--green-dark)"/>
          <stop offset="1" stop-color="var(--green-light)"/>
        </linearGradient>
      </defs>
      <path d="M40 352 C250 305 480 255 640 160 L640 192 C480 272 260 322 40 352Z" fill="url(#swooshGreenB)"/>
      <path d="M390 272 C510 245 600 170 640 50 L640 130 C590 205 500 252 390 272Z" fill="var(--green-dark)"/>
    </svg>
    <p class="brand-name"><span class="brand-name__dot"></span>Bright Meadows</p>
  </section>

</main>
</body>
</html>
```